Electrician Company Website Design

I am looking to get a website designed only. I do not need it converted ot html. I simply need the design in a psd format. I have my own team for the conversion. The website is for an electrician company called Bramblecourt electric. I have created a txt document with the project parameters and specifics. I have also uploaded their logo in all avaible formats. It's a zip file.

Number of Pages Required

1 page

```html
<!DOCTYPE html>
<html lang="en">
<head>
<meta charset="utf-8">
<title>Bramblecourt Electric — Website Design</title>
<link href="https://fonts.googleapis.com/css2?family=Open+Sans:ital,wght@0,400;0,600;0,700;0,800;1,700&display=swap" rel="stylesheet">
<style>
:root{
  --red:#8e1b1b;
  --yellow:#f5c400;
  --yellow-soft:#f7e38a;
  --grey-soft:#9a9a9a;
  --ink:#2d2d2d;
  --muted:#8a8a8a;
  --nav:#262626;
  --board:#333333;
  --soft:#f4f4f4;
  --line:#e2e2e2;
  --link:#7fb2ff;
  --white:#ffffff;
}
*{margin:0;padding:0;box-sizing:border-box}
html,body{width:1200px;height:2264px;overflow:hidden;background:var(--board)}
body{font-family:"Open Sans",Arial,sans-serif;color:var(--ink)}
.board{position:absolute;left:0;top:0;width:1365px;height:2576px;transform:scale(0.87912);transform-origin:0 0;background:var(--board)}
.page{position:absolute;top:0;overflow:hidden;background:var(--white)}
.page-lg{left:0;width:772px;height:2576px}
.page-sm{left:790px;width:540px;height:2548px}
.abs{position:absolute}
.center{text-align:center}
.photo{position:absolute}
.accent-block{position:absolute}
.accent-yellow{background:var(--yellow-soft)}
.accent-grey{background:linear-gradient(180deg,#b9b9b9,#a8a8a8)}
.topbar{position:absolute;left:0;top:0;width:100%;background:linear-gradient(100deg,#cfcfcf,#ededed 45%,#dadada)}
.brand{position:absolute;display:flex;align-items:center;gap:6px;font-weight:800;color:#1e1e1e;letter-spacing:.5px;text-transform:uppercase;white-space:nowrap}
.brand-dot{border-radius:50%;background:#1e1e1e;flex:none}
.call{position:absolute;top:0;background:var(--red);color:var(--white);display:flex;align-items:center;justify-content:center;gap:5px;font-weight:600;text-transform:uppercase;white-space:nowrap}
.social{position:absolute;border-radius:50%;background:#2f2f2f}
.nav{position:absolute;left:0;width:100%;background:var(--nav);display:flex;align-items:center;color:var(--white);text-transform:uppercase;white-space:nowrap}
.hero{background:radial-gradient(circle at 30% 15%,rgba(255,190,90,.55),transparent 18%),radial-gradient(circle at 55% 40%,rgba(255,170,70,.45),transparent 16%),radial-gradient(circle at 82% 20%,rgba(255,180,80,.4),transparent 15%),radial-gradient(circle at 52% 85%,rgba(255,200,120,.45),transparent 12%),linear-gradient(180deg,#3a261a,#2a1c14 60%,#3b2a20)}
.hero-title{position:absolute;color:var(--white);font-weight:700;letter-spacing:1px;text-transform:uppercase;white-space:nowrap}
.hero-sub{position:absolute;color:var(--white);text-transform:uppercase;white-space:nowrap}
.btn-ghost{position:absolute;color:var(--white);text-transform:uppercase}
.btn-grey{position:absolute;background:#6d6d6d;color:var(--white);text-transform:uppercase;display:flex;align-items:center;justify-content:center}
.strip{position:absolute;color:var(--white)}
.strip h4{font-weight:600;text-transform:uppercase;white-space:nowrap}
.strip p{color:#d0d0d0}
.strip .more{position:absolute;color:var(--link);font-weight:600}
.kicker{position:absolute;left:0;width:100%;text-align:center;color:#444;text-transform:uppercase}
.heading{position:absolute;left:0;width:100%;text-align:center;font-weight:700;color:#333}
.benefit{position:absolute;border:1px solid var(--line);background:var(--white);text-align:center;color:#444}
.btn-red{position:absolute;background:var(--red);color:var(--white);text-transform:uppercase;display:flex;align-items:center;justify-content:center}
.card h3{position:absolute;color:var(--white);font-weight:700;line-height:1.05;white-space:nowrap}
.card p{position:absolute;color:var(--white);white-space:nowrap}
.panel-photo{background:linear-gradient(180deg,#6f6a4a,#8b7c55 35%,#c9c1b0 55%,#7a7060)}
.plug-photo{background:linear-gradient(160deg,#4a4a4a,#5a5a5a 50%,#3a3a3a)}
.wire-photo{background:linear-gradient(170deg,#3c3a36,#5b5848 40%,#3e4a52 70%,#2c2c2c)}
.sky-photo{background:linear-gradient(180deg,#2c6fd6,#4c8ee6 55%,#7a6c5f 75%,#5d5045)}
.btn-outline{position:absolute;border:1px solid var(--red);color:var(--red);text-transform:uppercase;display:flex;align-items:center;justify-content:center;background:var(--white)}
.stat b{display:block;color:var(--yellow);font-weight:700;line-height:1;white-space:nowrap}
.stat span{display:block;color:#333;white-space:nowrap}
.tabs{position:absolute;display:flex;text-transform:uppercase;color:#333;white-space:nowrap}
.tabs span{display:flex;align-items:center;padding:0 7px;background:#f2f2f2}
.tabs .active{background:var(--red);color:var(--white)}
.svc h5{font-weight:700;color:#222}
.svc p{color:#888}
.tower-photo{background:linear-gradient(180deg,#1c2b45,#2d4566 60%,#3d5574)}
.pole-photo{background:linear-gradient(120deg,#cfcfcf,#e4e4e4 50%,#bdbdbd)}
.testi{background:linear-gradient(180deg,#2f2f2f,#2f2f2f 40%,#232323 40%,#232323 62%,#303030 62%)}
.testi-text{position:absolute;color:var(--white);text-align:center}
.avatar{position:absolute;border-radius:50%;background:#6b4a44}
.person{position:absolute;border-radius:50%}
.staff h5{font-weight:700;color:#222}
.staff span,.staff p{color:#666;display:block}
.gallery-1{background:linear-gradient(180deg,#9fb7c5,#5d7a58)}
.gallery-2{background:linear-gradient(180deg,#2e6fb8,#5b8fd0)}
.gallery-3{background:linear-gradient(180deg,#d8c6a0,#b4342c 45%,#cbb890)}
.gallery-4{background:linear-gradient(180deg,#7a8a72,#5f6e5e)}
.newsletter{position:absolute;background:var(--yellow);display:flex;align-items:center}
.footer{position:absolute;left:0;background:#1d1d1d;color:#cfcfcf}
.footer a{color:#cfcfcf;text-decoration:none;display:block}
.map{background:linear-gradient(135deg,#eef0e8,#dfe7ef 60%,#e8efe2)}
</style>
</head>
<body>
<div class="board">

<!-- ================= DESKTOP PAGE ================= -->
<main class="page page-lg">
  <header class="topbar" style="height:79px">
    <div class="brand" style="left:45px;top:22px;font-size:13px"><span class="brand-dot" style="width:26px;height:26px"></span>Bramblecourt Electric</div>
    <div class="call" style="left:500px;width:205px;height:30px;font-size:12px">
      <svg width="16" height="16" viewBox="0 0 16 16"><circle cx="8" cy="8" r="7" fill="none" stroke="#fff" stroke-width="1.3"/><path d="M5.3 4.5l1.4-.3.8 1.8-.9.7c.4.9 1 1.5 1.9 1.9l.7-.9 1.8.8-.3 1.4c-2.9.2-5.6-2.5-5.4-5.4z" fill="#fff"/></svg>
      Call us now 555 214 0198</div>
    <span class="social" style="left:639px;top:46px;width:18px;height:18px"></span>
    <span class="social" style="left:663px;top:46px;width:18px;height:18px"></span>
    <span class="social" style="left:688px;top:46px;width:18px;height:18px"></span>
  </header>
  <nav class="nav" style="top:79px;height:28px;font-size:11.5px;gap:20px;padding-left:333px">
    <span>Company</span><span>Service area</span><span>Services</span><span>Contact</span><span>Gallery</span><span>FAQ</span>
  </nav>
  <section class="photo hero" role="img" aria-label="Warm-lit vintage filament bulbs hanging from a wooden ceiling" style="left:0;top:107px;width:772px;height:417px"></section>
  <h1 class="hero-title" style="left:52px;top:236px;font-size:35px">Bramblecourt Electric</h1>
  <p class="hero-sub" style="left:55px;top:282px;font-size:10px;line-height:1.25">Lorem ipsum dolor sit amet, consectetur adipiscing elit, sed do eiusmod<br>tempor incididunt ut labore et dolore.</p>
  <span class="btn-ghost" style="left:68px;top:333px;font-size:10.5px">Learn more...</span>
  <span class="btn-grey" style="left:163px;top:326px;width:92px;height:26px;font-size:10.5px">Contact us</span>

  <div class="strip" style="left:43px;top:452px;width:233px;height:72px;background:#6a6a6a;padding:9px 9px 0 9px">
    <h4 style="font-size:10px">Commerical electrical services</h4>
    <p style="font-size:7.5px;margin-top:5px;line-height:1.5">Lorem ipsum dolor sit amet, consectetur adipiscing elit, sed do eiusmodmagna aliqua. Quis ipsum suspendisse facilisis.</p>
    <span class="more" style="right:24px;bottom:8px;font-size:7.5px">Read more...</span>
  </div>
  <div class="strip" style="left:276px;top:452px;width:234px;height:72px;background:#727272;padding:9px 9px 0 9px">
    <h4 style="font-size:10px">Residential electrical services</h4>
    <p style="font-size:7.5px;margin-top:5px;line-height:1.5">Lorem ipsum dolor sit amet, consectetur adipiscing elit, sed do eiusmod magna aliqua. Quis ipsum suspendisse facilisis.</p>
    <span class="more" style="right:11px;bottom:8px;font-size:7.5px">Read more...</span>
  </div>
  <div class="strip" style="left:510px;top:452px;width:262px;height:72px;background:#3a3a3a;padding:9px 16px 0 16px">
    <h4 style="font-size:10px">Industrial electrical services</h4>
    <p style="font-size:7.5px;margin-top:5px;line-height:1.5">Lorem ipsum dolor sit elit, sed do eiusmod tempor incididunt ut labore et dolore magna aliqua. Quis ipsum suspendisse facilisis.</p>
    <span class="more" style="right:36px;bottom:8px;font-size:7.5px">Read more...</span>
  </div>

  <p class="kicker" style="top:578px;font-size:15px">Our benefits</p>
  <h2 class="heading" style="top:601px;font-size:19px;line-height:1.22">Why We Should Be Your Top<br>Choice</h2>
  <div class="benefit" style="left:101px;top:668px;width:100px;height:89px">
    <svg class="abs" style="left:40px;top:10px" width="20" height="28" viewBox="0 0 20 28"><path d="M3 2h14M3 26h14M5 2c0 8 10 8 10 12S5 18 5 26M15 2c0 8-10 8-10 12s10 4 10 12" fill="none" stroke="#8e1b1b" stroke-width="2"/></svg>
    <p class="abs" style="left:0;width:100%;top:50px;font-size:11px;line-height:1.6">Quick Response<br>Times</p></div>
  <div class="benefit" style="left:219px;top:668px;width:100px;height:89px">
    <svg class="abs" style="left:38px;top:10px" width="24" height="28" viewBox="0 0 24 28"><rect x="2" y="2" width="16" height="22" fill="none" stroke="#8e1b1b" stroke-width="1.6"/><path d="M5 8h8M5 12h8M5 16h8" stroke="#8e1b1b" stroke-width="1.4"/><path d="M14 24l8-10" stroke="#8e1b1b" stroke-width="2"/></svg>
    <p class="abs" style="left:0;width:100%;top:50px;font-size:11px;line-height:1.6">Licensed<br>Electricians</p></div>
  <div class="benefit" style="left:337px;top:668px;width:99px;height:89px">
    <svg class="abs" style="left:35px;top:10px" width="30" height="30" viewBox="0 0 30 30"><circle cx="15" cy="15" r="12.5" fill="none" stroke="#8e1b1b" stroke-width="2"/><path d="M9 15l4.5 4.5L22 10" fill="none" stroke="#8e1b1b" stroke-width="2.2"/></svg>
    <p class="abs" style="left:0;width:100%;top:52px;font-size:11px;line-height:1.6">Experienced and<br>Accessible</p></div>
  <div class="benefit" style="left:454px;top:668px;width:99px;height:89px">
    <svg class="abs" style="left:36px;top:10px" width="28" height="30" viewBox="0 0 28 30"><path d="M7 2h14v8a7 7 0 0 1-14 0z" fill="#8e1b1b"/><path d="M7 5H2c0 5 3 7 6 7M21 5h5c0 5-3 7-6 7" fill="none" stroke="#8e1b1b" stroke-width="2"/><path d="M12 17h4v6h-4zM8 24h12v4H8z" fill="#8e1b1b"/></svg>
    <p class="abs" style="left:0;width:100%;top:52px;font-size:11px;line-height:1.6">Super Service<br>Award</p></div>
  <div class="benefit" style="left:574px;top:668px;width:99px;height:89px">
    <svg class="abs" style="left:35px;top:10px" width="30" height="30" viewBox="0 0 30 30"><circle cx="15" cy="15" r="12.5" fill="none" stroke="#8e1b1b" stroke-width="2"/><path d="M15 7v8h6" fill="none" stroke="#8e1b1b" stroke-width="2"/></svg>
    <p class="abs" style="left:0;width:100%;top:52px;font-size:11px;line-height:1.6">Over 60 yeras of<br>experience</p></div>
  <span class="btn-red" style="left:322px;top:788px;width:130px;height:29px;font-size:10px">More benefits</span>

  <section class="card">
    <div class="photo panel-photo" role="img" aria-label="Open electrical distribution panel with rows of breakers" style="left:0;top:875px;width:256px;height:317px"></div>
    <div class="photo plug-photo" role="img" aria-label="Black power plug in front of a wall outlet" style="left:256px;top:875px;width:256px;height:317px"></div>
    <div class="photo wire-photo" role="img" aria-label="Tangle of coloured wiring inside an industrial cabinet" style="left:512px;top:875px;width:260px;height:317px"></div>
    <h3 style="left:31px;top:906px;font-size:15.5px">Electrical Wiring And Re-<br>Wiring Experts</h3>
    <p style="left:35px;top:960px;font-size:11px;line-height:1.3">Lorem Ipsum is simply dummy text of<br>the printing and typesetting industry.</p>
    <span class="btn-red" style="left:36px;top:1118px;width:97px;height:38px;font-size:11px">Read more</span>
    <h3 style="left:291px;top:906px;font-size:15.5px">Whole House Generator<br>Installation &amp; Maintainane</h3>
    <p style="left:295px;top:960px;font-size:11px;line-height:1.3">Lorem Ipsum is simply dummy text of<br>the printing and typesetting industry.</p>
    <span class="btn-red" style="left:295px;top:1118px;width:97px;height:38px;font-size:11px">Read more</span>
    <h3 style="left:550px;top:906px;font-size:15.5px">Commercial &amp; Industrial<br>Services</h3>
    <p style="left:554px;top:960px;font-size:11px;line-height:1.3">Lorem Ipsum is simply dummy text of<br>the printing and typesetting industry.</p>
    <span class="btn-red" style="left:549px;top:1118px;width:97px;height:38px;font-size:11px">Read more</span>
  </section>

  <section class="abs" style="left:0;top:1192px;width:772px;height:413px;background:var(--soft)"></section>
  <div class="accent-block accent-yellow" role="img" aria-label="Decorative yellow accent" style="left:18px;top:1218px;width:110px;height:32px"></div>
  <div class="accent-block accent-grey" role="img" aria-label="Decorative grey accent" style="left:18px;top:1260px;width:44px;height:84px"></div>
  <div class="photo sky-photo" role="img" aria-label="Technician lifting a solar panel on a roof under blue sky" style="left:69px;top:1258px;width:278px;height:287px"></div>
  <svg class="abs" style="left:191px;top:1385px" width="32" height="32" viewBox="0 0 32 32"><circle cx="16" cy="16" r="14.5" fill="rgba(255,255,255,.15)" stroke="#222" stroke-width="1.6"/><path d="M13 10v12l9-6z" fill="none" stroke="#222" stroke-width="1.6"/></svg>
  <div class="accent-block accent-grey" role="img" aria-label="Decorative grey accent" style="left:356px;top:1515px;width:44px;height:28px"></div>
  <div class="accent-block accent-yellow" role="img" aria-label="Decorative yellow accent" style="left:338px;top:1553px;width:62px;height:32px"></div>
  <p class="abs" style="left:440px;top:1261px;font-size:15px;color:#555;text-transform:uppercase">About us</p>
  <h2 class="abs" style="left:438px;top:1284px;font-size:21.5px;font-weight:700;line-height:1.05;color:#222;white-space:nowrap">Experienced Electricians<br>Offering Quality Electrical<br>Services</h2>
  <p class="abs" style="left:438px;top:1361px;width:315px;font-size:11px;line-height:1.38;color:#9b9b9b">Lorem Ipsum is simply dummy text of the printing and typesetting industry. Lorem Ipsum has been the industry's standard dummy text ever since the 1500s,</p>
  <span class="btn-outline" style="left:438px;top:1418px;width:108px;height:31px;font-size:10px;color:#555">Read more</span>
  <div class="stat abs" style="left:438px;top:1478px"><b style="font-size:36px">8 <span style="display:inline;color:var(--yellow);font-weight:300">+</span></b><span style="font-size:11px;margin-top:9px">Years of experiance</span></div>
  <div class="stat abs" style="left:552px;top:1478px"><b style="font-size:36px">15 <span style="display:inline;color:var(--yellow);font-weight:300">+</span></b><span style="font-size:11px;margin-top:9px">Qualified specialist</span></div>
  <div class="stat abs center" style="left:671px;top:1478px"><b style="font-size:36px">11 <span style="display:inline;color:var(--yellow);font-weight:300">+</span></b><span style="font-size:11px;margin-top:4px;line-height:1.3">Partner<br>companies</span></div>

  <p class="kicker" style="top:1656px;font-size:15px">Services</p>
  <h2 class="heading" style="top:1680px;font-size:21px">If It Is Electrical, We Do It...</h2>
  <p class="abs center" style="left:0;width:772px;top:1716px;font-size:11px;color:var(--muted)">Lorem Ipsum is simply dummy text of the printing and typesetting industry.</p>
  <div class="tabs" style="left:167px;top:1755px;height:21px;font-size:10.5px"><span class="active">Residential electricians</span><span>Commercial electricians</span><span>Industrial electrician</span></div>
  <div class="svc abs" style="left:44px;top:1803px;width:220px;font-size:11px">
    <h5>Electrical Installation</h5><p style="margin-top:5px;line-height:1.4">Lorem Ipsum is simply dummy text of the printing and typesetting industry.</p>
    <h5 style="margin-top:19px">Additon / Renovation Wiring</h5><p style="margin-top:5px;line-height:1.4">Lorem Ipsum is simply dummy text of the printing and typesetting industry.</p>
    <h5 style="margin-top:19px">Electrical Repairs</h5><p style="margin-top:5px;line-height:1.4">Lorem Ipsum is simply dummy text of the printing and typesetting industry.</p>
  </div>
  <div class="svc abs" style="left:306px;top:1803px;width:220px;font-size:11px">
    <h5>Lighting</h5><p style="margin-top:5px;line-height:1.4">Lorem Ipsum is simply dummy text of the printing and typesetting industry.</p>
    <h5 style="margin-top:19px">Home Generatiors</h5><p style="margin-top:5px;line-height:1.4">Lorem Ipsum is simply dummy text of the printing and typesetting industry.</p>
    <h5 style="margin-top:19px">Circuit Breaker Panels</h5><p style="margin-top:5px;line-height:1.4">Lorem Ipsum is simply dummy text of the printing and typesetting industry.</p>
  </div>
  <div class="photo tower-photo" role="img" aria-label="Steel transmission tower against a night sky" style="left:564px;top:1805px;width:178px;height:195px"></div>

  <section class="photo testi" style="left:0;top:2047px;width:772px;height:318px"></section>
  <div class="photo pole-photo" role="img" aria-label="Black and white power line insulators on a utility pole" style="left:0;top:2047px;width:363px;height:318px"></div>
  <p class="testi-text" style="left:400px;width:372px;top:2128px;font-size:10px;text-transform:uppercase">Testimonials</p>
  <p class="testi-text" style="left:380px;width:392px;top:2148px;font-size:17px;font-weight:700;font-style:italic">Clients Say</p>
  <p class="testi-text" style="left:400px;width:364px;top:2185px;font-size:13px;line-height:1.35">Lorem Ipsum is simply dummy text of the<br>printing and typesetting industry.</p>
  <span class="avatar" role="img" aria-label="Client portrait" style="left:548px;top:2226px;width:44px;height:44px"></span>
  <p class="testi-text" style="left:400px;width:372px;top:2294px;font-size:11px"><span style="color:var(--red)">Dana Morrow</span> Nw jersey</p>

  <p class="kicker" style="top:2405px;font-size:15px">Our staff</p>
  <h2 class="heading" style="top:2432px;font-size:20px;line-height:1.2">Our Professional Electrician<br>&nbsp;Staff</h2>
  <span class="person" role="img" aria-label="Staff portrait" style="left:88px;top:2525px;width:142px;height:142px;background:#3b2f2c"></span>
  <span class="person" role="img" aria-label="Staff portrait" style="left:316px;top:2525px;width:142px;height:142px;background:#9a8c80"></span>
  <span class="person" role="img" aria-label="Staff portrait" style="left:546px;top:2525px;width:142px;height:142px;background:#dfe6e8"></span>
</main>

<!-- ================= COMPACT PAGE ================= -->
<main class="page page-sm">
  <header class="topbar" style="height:58px">
    <div class="brand" style="left:30px;top:16px;font-size:9.5px"><span class="brand-dot" style="width:18px;height:18px"></span>Bramblecourt Electric</div>
    <div class="call" style="left:350px;width:143px;height:22px;font-size:8.5px">
      <svg width="12" height="12" viewBox="0 0 16 16"><circle cx="8" cy="8" r="7" fill="none" stroke="#fff" stroke-width="1.3"/><path d="M5.3 4.5l1.4-.3.8 1.8-.9.7c.4.9 1 1.5 1.9 1.9l.7-.9 1.8.8-.3 1.4c-2.9.2-5.6-2.5-5.4-5.4z" fill="#fff"/></svg>
      Call us now 555 214 0198</div>
    <span class="social" style="left:447px;top:35px;width:12px;height:12px"></span>
    <span class="social" style="left:464px;top:35px;width:12px;height:12px"></span>
    <span class="social" style="left:481px;top:35px;width:12px;height:12px"></span>
  </header>
  <nav class="nav" style="top:58px;height:19px;font-size:7.5px;gap:14px;padding-left:233px">
    <span>Company</span><span>Service area</span><span>Services</span><span>Contact</span><span>Gallery</span><span>FAQ</span>
  </nav>
  <section class="photo hero" role="img" aria-label="Warm-lit vintage filament bulbs hanging from a wooden ceiling" style="left:0;top:77px;width:540px;height:291px"></section>
  <h1 class="hero-title" style="left:37px;top:164px;font-size:25px">Bramblecourt Electric</h1>
  <p class="hero-sub" style="left:38px;top:198px;font-size:7px;line-height:1.25">Lorem ipsum dolor sit amet, consectetur adipiscing elit, sed do eiusmod<br>tempor incididunt ut labore et dolore.</p>
  <span class="btn-ghost" style="left:48px;top:234px;font-size:7px">Learn more...</span>
  <span class="btn-grey" style="left:115px;top:231px;width:63px;height:17px;font-size:7px">Contact us</span>

  <div class="strip" style="left:30px;top:318px;width:163px;height:50px;background:#6a6a6a;padding:6px 6px 0 6px">
    <h4 style="font-size:7px">Commerical electrical services</h4>
    <p style="font-size:5.5px;margin-top:4px;line-height:1.5">Lorem ipsum dolor sit amet, consectetur adipiscing elit, sed do eiusmodmagna aliqua. Quis ipsum suspendisse facilisis.</p>
    <span class="more" style="right:16px;bottom:4px;font-size:5.5px">Read more...</span>
  </div>
  <div class="strip" style="left:193px;top:318px;width:167px;height:50px;background:#727272;padding:6px 8px 0 8px">
    <h4 style="font-size:7px">Residential electrical services</h4>
    <p style="font-size:5.5px;margin-top:4px;line-height:1.5">Lorem ipsum dolor sit amet, consectetur adipiscing elit, sed do eiusmod magna aliqua. Quis ipsum suspendisse facilisis.</p>
    <span class="more" style="right:8px;bottom:4px;font-size:5.5px">Read more...</span>
  </div>
  <div class="strip" style="left:360px;top:318px;width:160px;height:50px;background:#3a3a3a;padding:6px 8px 0 8px">
    <h4 style="font-size:7px">Industrial electrical services</h4>
    <p style="font-size:5.5px;margin-top:4px;line-height:1.5">Lorem ipsum dolor sit elit, sed do eiusmod tempor incididunt ut labore et dolore magna aliqua. Quis ipsum suspendisse facilisis.</p>
    <span class="more" style="right:8px;bottom:4px;font-size:5.5px">Read more...</span>
  </div>
  <div class="abs" style="left:520px;top:318px;width:20px;height:50px;background:#2a2a2a"></div>

  <p class="kicker" style="top:407px;font-size:10px">Our benefits</p>
  <h2 class="heading" style="top:422px;font-size:13.5px;line-height:1.25">Why We Should Be Your Top<br>Choice</h2>
  <div class="benefit" style="left:71px;top:470px;width:70px;height:61px">
    <svg class="abs" style="left:29px;top:7px" width="13" height="19" viewBox="0 0 20 28"><path d="M3 2h14M3 26h14M5 2c0 8 10 8 10 12S5 18 5 26M15 2c0 8-10 8-10 12s10 4 10 12" fill="none" stroke="#8e1b1b" stroke-width="2.4"/></svg>
    <p class="abs" style="left:0;width:100%;top:34px;font-size:7.5px;line-height:1.6">Quick Response<br>Times</p></div>
  <div class="benefit" style="left:153px;top:470px;width:70px;height:61px">
    <svg class="abs" style="left:27px;top:7px" width="16" height="19" viewBox="0 0 24 28"><rect x="2" y="2" width="16" height="22" fill="none" stroke="#8e1b1b" stroke-width="1.8"/><path d="M5 8h8M5 12h8M5 16h8" stroke="#8e1b1b" stroke-width="1.6"/><path d="M14 24l8-10" stroke="#8e1b1b" stroke-width="2.2"/></svg>
    <p class="abs" style="left:0;width:100%;top:34px;font-size:7.5px;line-height:1.6">Licensed<br>Electricians</p></div>
  <div class="benefit" style="left:236px;top:470px;width:70px;height:61px">
    <svg class="abs" style="left:25px;top:7px" width="20" height="20" viewBox="0 0 30 30"><circle cx="15" cy="15" r="12.5" fill="none" stroke="#8e1b1b" stroke-width="2.4"/><path d="M9 15l4.5 4.5L22 10" fill="none" stroke="#8e1b1b" stroke-width="2.6"/></svg>
    <p class="abs" style="left:0;width:100%;top:34px;font-size:7.5px;line-height:1.6">Experienced and<br>Accessible</p></div>
  <div class="benefit" style="left:318px;top:470px;width:70px;height:61px">
    <svg class="abs" style="left:25px;top:7px" width="19" height="20" viewBox="0 0 28 30"><path d="M7 2h14v8a7 7 0 0 1-14 0z" fill="#8e1b1b"/><path d="M7 5H2c0 5 3 7 6 7M21 5h5c0 5-3 7-6 7" fill="none" stroke="#8e1b1b" stroke-width="2.4"/><path d="M12 17h4v6h-4zM8 24h12v4H8z" fill="#8e1b1b"/></svg>
    <p class="abs" style="left:0;width:100%;top:34px;font-size:7.5px;line-height:1.6">Super Service<br>Award</p></div>
  <div class="benefit" style="left:400px;top:470px;width:70px;height:61px">
    <svg class="abs" style="left:25px;top:7px" width="20" height="20" viewBox="0 0 30 30"><circle cx="15" cy="15" r="12.5" fill="none" stroke="#8e1b1b" stroke-width="2.4"/><path d="M15 7v8h6" fill="none" stroke="#8e1b1b" stroke-width="2.4"/></svg>
    <p class="abs" style="left:0;width:100%;top:34px;font-size:7.5px;line-height:1.6">Over 60 yeras of<br>experience</p></div>
  <span class="btn-red" style="left:225px;top:553px;width:91px;height:20px;font-size:7px">More benefits</span>

  <section class="card">
    <div class="photo panel-photo" role="img" aria-label="Open electrical distribution panel with rows of breakers" style="left:0;top:614px;width:180px;height:221px"></div>
    <div class="photo plug-photo" role="img" aria-label="Black power plug in front of a wall outlet" style="left:180px;top:614px;width:180px;height:221px"></div>
    <div class="photo wire-photo" role="img" aria-label="Tangle of coloured wiring inside an industrial cabinet" style="left:360px;top:614px;width:180px;height:221px"></div>
    <h3 style="left:22px;top:636px;font-size:11px">Electrical Wiring And Re-<br>Wiring Experts</h3>
    <p style="left:25px;top:673px;font-size:7.5px;line-height:1.3">Lorem Ipsum is simply dummy text of<br>the printing and typesetting industry.</p>
    <span class="btn-red" style="left:27px;top:784px;width:65px;height:26px;font-size:7.5px">Read more</span>
    <h3 style="left:203px;top:636px;font-size:11px">Whole House Generator<br>Installation &amp; Maintainane</h3>
    <p style="left:206px;top:673px;font-size:7.5px;line-height:1.3">Lorem Ipsum is simply dummy text of<br>the printing and typesetting industry.</p>
    <span class="btn-red" style="left:207px;top:784px;width:67px;height:26px;font-size:7.5px">Read more</span>
    <h3 style="left:384px;top:636px;font-size:11px">Commercial &amp; Industrial<br>Services</h3>
    <p style="left:387px;top:673px;font-size:7.5px;line-height:1.3">Lorem Ipsum is simply dummy text of<br>the printing and typesetting industry.</p>
    <span class="btn-red" style="left:385px;top:784px;width:66px;height:26px;font-size:7.5px">Read more</span>
  </section>

  <section class="abs" style="left:0;top:835px;width:540px;height:288px;background:var(--soft)"></section>
  <div class="accent-block accent-yellow" role="img" aria-label="Decorative yellow accent" style="left:13px;top:853px;width:78px;height:23px"></div>
  <div class="accent-block accent-grey" role="img" aria-label="Decorative grey accent" style="left:13px;top:883px;width:31px;height:59px"></div>
  <div class="photo sky-photo" role="img" aria-label="Technician lifting a solar panel on a roof under blue sky" style="left:49px;top:881px;width:194px;height:201px"></div>
  <svg class="abs" style="left:134px;top:970px" width="22" height="22" viewBox="0 0 32 32"><circle cx="16" cy="16" r="14.5" fill="rgba(255,255,255,.15)" stroke="#222" stroke-width="2"/><path d="M13 10v12l9-6z" fill="none" stroke="#222" stroke-width="2"/></svg>
  <div class="accent-block accent-grey" role="img" aria-label="Decorative grey accent" style="left:248px;top:1061px;width:31px;height:20px"></div>
  <div class="accent-block accent-yellow" role="img" aria-label="Decorative yellow accent" style="left:235px;top:1088px;width:44px;height:23px"></div>
  <p class="abs" style="left:308px;top:884px;font-size:10px;color:#555;text-transform:uppercase">About us</p>
  <h2 class="abs" style="left:307px;top:899px;font-size:15px;font-weight:700;line-height:1.05;color:#222;white-space:nowrap">Experienced Electricians<br>Offering Quality Electrical<br>Services</h2>
  <p class="abs" style="left:307px;top:953px;width:222px;font-size:7.5px;line-height:1.4;color:#9b9b9b">Lorem Ipsum is simply dummy text of the printing and typesetting industry. Lorem Ipsum has been the industry's standard dummy text ever since the 1500s,</p>
  <span class="btn-outline" style="left:307px;top:994px;width:76px;height:21px;font-size:7px;color:#555">Read more</span>
  <div class="stat abs" style="left:306px;top:1036px"><b style="font-size:25px">8 <span style="display:inline;color:var(--yellow);font-weight:300">+</span></b><span style="font-size:7.5px;margin-top:6px">Years of experiance</span></div>
  <div class="stat abs" style="left:391px;top:1036px"><b style="font-size:25px">15 <span style="display:inline;color:var(--yellow);font-weight:300">+</span></b><span style="font-size:7.5px;margin-top:6px">Qualified specialist</span></div>
  <div class="stat abs center" style="left:470px;top:1036px"><b style="font-size:25px">11 <span style="display:inline;color:var(--yellow);font-weight:300">+</span></b><span style="font-size:7.5px;margin-top:2px;line-height:1.3">Partner<br>companies</span></div>

  <p class="kicker" style="top:1160px;font-size:10px">Services</p>
  <h2 class="heading" style="top:1176px;font-size:14.5px">If It Is Electrical, We Do It...</h2>
  <p class="abs center" style="left:0;width:540px;top:1201px;font-size:7.5px;color:var(--muted)">Lorem Ipsum is simply dummy text of the printing and typesetting industry.</p>
  <div class="tabs" style="left:117px;top:1229px;height:14px;font-size:7px"><span class="active">Residential electricians</span><span>Commercial electricians</span><span>Industrial electrician</span></div>
  <div class="svc abs" style="left:31px;top:1262px;width:155px;font-size:7.5px">
    <h5>Electrical Installation</h5><p style="margin-top:3px;line-height:1.4">Lorem Ipsum is simply dummy text of the printing and typesetting industry.</p>
    <h5 style="margin-top:13px">Additon / Renovation Wiring</h5><p style="margin-top:3px;line-height:1.4">Lorem Ipsum is simply dummy text of the printing and typesetting industry.</p>
    <h5 style="margin-top:13px">Electrical Repairs</h5><p style="margin-top:3px;line-height:1.4">Lorem Ipsum is simply dummy text of the printing and typesetting industry.</p>
  </div>
  <div class="svc abs" style="left:214px;top:1262px;width:155px;font-size:7.5px">
    <h5>Lighting</h5><p style="margin-top:3px;line-height:1.4">Lorem Ipsum is simply dummy text of the printing and typesetting industry.</p>
    <h5 style="margin-top:13px">Home Generatiors</h5><p style="margin-top:3px;line-height:1.4">Lorem Ipsum is simply dummy text of the printing and typesetting industry.</p>
    <h5 style="margin-top:13px">Circuit Breaker Panels</h5><p style="margin-top:3px;line-height:1.4">Lorem Ipsum is simply dummy text of the printing and typesetting industry.</p>
  </div>
  <div class="photo tower-photo" role="img" aria-label="Steel transmission tower against a night sky" style="left:393px;top:1263px;width:145px;height:137px"></div>

  <section class="photo testi" style="left:0;top:1433px;width:540px;height:222px"></section>
  <div class="photo pole-photo" role="img" aria-label="Black and white power line insulators on a utility pole" style="left:0;top:1433px;width:254px;height:222px"></div>
  <p class="testi-text" style="left:280px;width:260px;top:1486px;font-size:7px;text-transform:uppercase">Testimonials</p>
  <p class="testi-text" style="left:265px;width:275px;top:1502px;font-size:11.5px;font-weight:700">Clients Say</p>
  <p class="testi-text" style="left:280px;width:255px;top:1528px;font-size:8.5px;line-height:1.4">Lorem Ipsum is simply dummy text of the<br>printing and typesetting industry.</p>
  <span class="avatar" role="img" aria-label="Client portrait" style="left:383px;top:1558px;width:30px;height:30px"></span>
  <p class="testi-text" style="left:280px;width:260px;top:1603px;font-size:7.5px"><span style="color:var(--red)">Dana Morrow</span> Nw jersey</p>

  <p class="kicker" style="top:1682px;font-size:10px">Our staff</p>
  <h2 class="heading" style="top:1699px;font-size:14px;line-height:1.22">Our Professional Electrician<br>&nbsp;Staff</h2>
  <span class="person" role="img" aria-label="Staff portrait" style="left:59px;top:1766px;width:104px;height:104px;background:#3b2f2c"></span>
  <span class="person" role="img" aria-label="Staff portrait" style="left:219px;top:1766px;width:104px;height:104px;background:#9a8c80"></span>
  <span class="person" role="img" aria-label="Staff portrait" style="left:378px;top:1766px;width:104px;height:104px;background:#dfe6e8"></span>
  <div class="staff abs center" style="left:51px;top:1893px;width:120px"><h5 style="font-size:10.5px">Marcus Hale</h5><span style="font-size:7px;margin-top:5px">Installation</span><p style="font-size:7px;margin-top:4px;line-height:1.3">Lorem ipsum dolor sit amet consectuetur adipscing elit sed euismod tempor.</p></div>
  <div class="staff abs center" style="left:211px;top:1893px;width:120px"><h5 style="font-size:10.5px">Owen Pritchard</h5><span style="font-size:7px;margin-top:5px">Installation</span><p style="font-size:7px;margin-top:4px;line-height:1.3">Lorem ipsum dolor sit amet consectuetur adipscing elit sed euismod tempor.</p></div>
  <div class="staff abs center" style="left:370px;top:1893px;width:120px"><h5 style="font-size:10.5px">Ravi Castell</h5><span style="font-size:7px;margin-top:5px">Installation</span><p style="font-size:7px;margin-top:4px;line-height:1.3">Lorem ipsum dolor sit amet consectuetur adipscing elit sed euismod tempor.</p></div>

  <p class="abs center" style="left:0;width:540px;top:2024px;font-size:10px;font-weight:700;text-transform:uppercase;color:#222">Our gallery</p>
  <p class="abs center" style="left:0;width:540px;top:2040px;font-size:7.5px;color:var(--muted)">Lorem Ipsum is simply dummy text of the printing and typesetting industry.</p>
  <div class="photo gallery-1" role="img" aria-label="Lineworker repairing wires atop a utility pole" style="left:0;top:2066px;width:134px;height:170px"></div>
  <div class="photo gallery-2" role="img" aria-label="Looking up through a transmission tower at blue sky" style="left:134px;top:2066px;width:134px;height:170px"></div>
  <div class="photo gallery-3" role="img" aria-label="High voltage danger sign on a metal door" style="left:268px;top:2066px;width:134px;height:170px"></div>
  <div class="photo gallery-4" role="img" aria-label="Green industrial switchgear control panels" style="left:402px;top:2066px;width:138px;height:170px"></div>

  <footer class="footer" style="top:2306px;width:540px;height:242px"></footer>
  <div class="newsletter" style="left:53px;top:2288px;width:438px;height:44px">
    <svg class="abs" style="left:12px;top:14px" width="22" height="16" viewBox="0 0 22 16"><rect width="22" height="16" fill="#222"/><path d="M0 0l11 8 11-8" fill="none" stroke="#f5c400" stroke-width="1.5"/></svg>
    <p class="abs" style="left:60px;top:10px;font-size:9.5px;color:#333;white-space:nowrap">Subscribe to our Newsletter</p>
    <p class="abs" style="left:61px;top:25px;font-size:6px;color:#555;white-space:nowrap">You will only receive news and discounts</p>
    <span class="abs" style="left:232px;top:12px;width:174px;height:20px;background:var(--white);font-size:6.5px;color:#666;padding:5px 0 0 16px">Enter your e-mail address</span>
    <span class="abs" style="left:406px;top:12px;width:22px;height:20px;background:#222"><svg width="22" height="20" viewBox="0 0 22 20"><path d="M9 6l4 4-4 4" fill="none" stroke="#fff" stroke-width="1.5"/></svg></span>
  </div>
  <div class="brand" style="left:32px;top:2372px;font-size:8px;color:#555"><span class="brand-dot" style="width:14px;height:14px;background:#555"></span>Bramblecourt Electric</div>
  <div class="footer abs" style="left:33px;top:2424px;font-size:7px;line-height:2.4;text-transform:uppercase;background:none"><a>Company</a><a>Service area</a><a>Services</a><a>Contact</a></div>
  <div class="footer abs" style="left:112px;top:2424px;font-size:7px;line-height:2.4;text-transform:uppercase;background:none"><a>Gallery</a><a>FAQs</a></div>
  <p class="abs" style="left:178px;top:2374px;font-size:7px;line-height:1.7;color:#cfcfcf">Lorem Ipsum is simply dummy text of<br>the printing and typesetting industry.</p>
  <svg class="abs" style="left:180px;top:2424px" width="10" height="13" viewBox="0 0 10 13"><path d="M5 0a5 5 0 0 1 5 5c0 3-5 8-5 8S0 8 0 5a5 5 0 0 1 5-5z" fill="#cfcfcf"/><circle cx="5" cy="5" r="2" fill="#1d1d1d"/></svg>
  <p class="abs" style="left:197px;top:2422px;font-size:6.5px;line-height:1.6;color:#cfcfcf">1420 Alder Ridge Rd<br>Northfield, MN 55000</p>
  <svg class="abs" style="left:179px;top:2459px" width="12" height="9" viewBox="0 0 12 9"><rect width="12" height="9" fill="#cfcfcf"/><path d="M0 0l6 5 6-5" fill="none" stroke="#1d1d1d" stroke-width="1"/></svg>
  <p class="abs" style="left:197px;top:2456px;font-size:6.5px;line-height:1.6;color:#cfcfcf">info@bramblecourt<br>electric.com</p>
  <svg class="abs" style="left:181px;top:2491px" width="9" height="10" viewBox="0 0 16 16"><path d="M3 1l3-.5 1.5 3.5-1.8 1.4c.8 1.8 2 3 3.8 3.8L11 7.5l3.5 1.5L14 12C8 12.5 2.5 7 3 1z" fill="#cfcfcf"/></svg>
  <p class="abs" style="left:197px;top:2492px;font-size:6.5px;color:#cfcfcf">555 214 0198</p>
  <div class="photo map" role="img" aria-label="Street map showing the office location" style="left:335px;top:2378px;width:183px;height:95px"></div>
  <span class="social" style="left:471px;top:2512px;width:12px;height:12px;background:#cfcfcf"></span>
  <span class="social" style="left:488px;top:2512px;width:12px;height:12px;background:#cfcfcf"></span>
  <span class="social" style="left:506px;top:2512px;width:12px;height:12px;background:#cfcfcf"></span>
  <p class="abs" style="left:33px;top:2530px;font-size:6.5px;color:#cfcfcf">Bramblecourt electric 2022 All Right Reserved</p>
</main>

</div>
</body>
</html>
```